TUSK needs a simple, contemporary and easy to use 'designer' website (fully working/coded)

TUSK is a progressive market research consultancy based in Sydney, Australia. We are a new company and require a contemporary/modern and bold, uncomplicated/simple, clean/uncluttered site, which uses friendly and easy to read fonts. The brand is approachable. The colour palate should be simple and contemporary. Colours used in our logo are:#FFCC00 and #404041 so any others should complement these.

The following website gives a really good idea of how simple the site should be: www.brightquarrel.com.au and I am looking to create something similar to this style of site (but not necessarily copied).

The website should convey ‘different types of customer’. TUSK helps different companies ‘connect’ with their particular shoppers or end users of their product. This could be a mum doing the washing, a dad cleaning the car, children eating ice cream, old people reading the newspaper, someone trying on glasses, someone buying petfood etc. Alternatively it could simply just be pictures of different people…different ages, different nationalities, different employment types etc, but they should give a positive impression (ie people smiling/laughing) and also GREAT quality photos.

Content will also be attached but please note this is just a draft reference and will be sent to a copywriter for improvement. The telephone number is yet to be confirmed but will be given at the end of the contest.

The navigation may borrow strongly from www.brightquarrel.com.au. It may have the following navigation panel:

ABOUT US

WHAT WE DO

> NPD

> PRODUCT TESTING

> SHOPPER

> SEGMENTATION

> ONLINE COMMUNITIES

> CUSTOMER EXPERIENCE

> VISUALISATION

> TAILOR MADE

CONTACT US

The home page may be WHAT WE DO and each picture represents one of the 8 sections (such as NPD) etc.

One of my main objectives is also to get people to sign up to my quarterly newsletter, so would like to make this very visible, and make it easy for them to connect via netlinker.

I will also want to add a blog page in September (so needs to be hidden now but switched on in Sept). This blog will contain articles from the newsletters and netlinker updates. I may also want to add a simple 90-180 second video at the bottom of each of the 8 sections (to be added over the next 12 months but i would like to ensure it is possible to do this at a later stage).

The logo has recently been designed and i have attcahed different colour versions as i may be swayed depending on hoe they look in te website. I tend to prefer yellow on white, or white on yellow but other optins are included if you think they work better with your design.

Target Market(s)

Professionals in large blue chip companies..such as fizzwell, marbury, hollanet etc. Marketing Managers/Directors, PR and advertising agencies etc.

Industry/Entity Type

Progressive

Requirements
Must have
• High quality positive photos. Be very easy to navigate...should scream simple!

```html
<!DOCTYPE html>
<html lang="en">
<head>
<meta charset="utf-8">
<title>TUSK – What We Do</title>
<link rel="stylesheet" href="https://fonts.googleapis.com/css2?family=Montserrat:wght@400;500;600&display=swap">
<style>
:root{
  --yellow:#fdcc0a;
  --charcoal:#3a3a3b;
  --text:#6b6b6c;
  --nav:#5a5a5b;
  --box:#7a7a7b;
  --white:#ffffff;
}
*{margin:0;padding:0;box-sizing:border-box}
html,body{width:1200px;height:699px;overflow:hidden;background:var(--white);font-family:"Montserrat",sans-serif}
.canvas{position:relative;width:1200px;height:699px;overflow:hidden}

.sidebar{position:absolute;left:0;top:0;width:266px;height:699px;background:var(--white);box-shadow:4px 0 14px rgba(0,0,0,.18);z-index:3;border-right:1px solid #ddd}
.brand{position:absolute;left:33px;top:44px;font-size:38px;font-weight:500;color:var(--charcoal);letter-spacing:4px;line-height:1}
.brand-tag{position:absolute;left:33px;top:95px;font-size:12.5px;color:var(--charcoal)}

.nav{position:absolute;left:36px;top:166px;list-style:none}
.nav-main{font-size:12.5px;font-weight:600;color:var(--nav);height:31px;line-height:18px}
.nav-sub{list-style:none;margin:-4px 0 4px}
.nav-sub li{font-size:12.5px;color:var(--nav);height:30.4px;padding-left:14px;position:relative;line-height:18px;letter-spacing:.2px}
.nav-sub li::before{content:"";position:absolute;left:1px;top:6px;width:5px;height:5px;border-top:1px solid #aaa;border-right:1px solid #aaa;transform:rotate(45deg)}
.nav-sub li.accent::before{border-color:var(--yellow)}
.nav-sub li.current{color:var(--yellow)}

.newsletter{position:absolute;left:30px;top:541px;width:206px;height:85px;background:var(--box);border-radius:2px;padding:12px 14px}
.newsletter h3{font-size:14.5px;font-weight:500;color:var(--white);letter-spacing:.4px}
.signup{margin-top:9px;width:178px;height:29px;background:var(--white);border-radius:3px;position:relative}
.signup span{position:absolute;left:10px;top:6px;font-family:Georgia,serif;font-style:italic;font-size:12px;color:#666}
.signup svg{position:absolute;right:3px;top:3px}
.copyright{position:absolute;left:33px;top:641px;font-size:11.5px;color:#888}

.gallery{position:absolute;left:266px;top:0;width:934px;height:699px;display:grid;grid-template-columns:312px 311px 311px;grid-template-rows:233px 233px 233px}
.tile{background:linear-gradient(160deg,#d8d8d6,#bdbdbb)}
.tile:nth-child(2n){background:linear-gradient(200deg,#cfd0cc,#b4b6b2)}
.tile:nth-child(3n){background:linear-gradient(140deg,#dcdad6,#c4c0bb)}

.modal{position:absolute;left:295px;top:28px;width:876px;height:643px;background:var(--white);z-index:4;box-shadow:0 0 18px rgba(0,0,0,.15)}
.modal-head{height:74px;background:var(--yellow);padding:27px 28px}
.modal-head h1{font-size:19px;font-weight:500;color:#222;letter-spacing:.3px}
.close{position:absolute;right:0;top:0;width:26px;height:25px;background:var(--charcoal)}
.modal-body{position:absolute;left:29px;top:100px;width:822px;height:478px;overflow:hidden;font-size:13.2px;line-height:22.8px;color:var(--text)}
.modal-body p{margin-bottom:22.8px}
.modal-body strong{color:var(--charcoal);font-weight:600}
.scrollbar{position:absolute;left:858px;top:102px;width:12px;height:156px;background:var(--yellow)}
.modal-foot{position:absolute;left:0;bottom:0;width:100%;height:38px;background:var(--charcoal)}
</style>
</head>
<body>
<div class="canvas">
  <aside class="sidebar">
    <div class="brand">TUSK</div>
    <div class="brand-tag">progressive research</div>
    <ul class="nav">
      <li class="nav-main">ABOUT US</li>
      <li class="nav-main">WHAT WE DO</li>
      <li>
        <ul class="nav-sub">
          <li class="current accent">NPD</li>
          <li>PRODUCT TESTING</li>
          <li>SHOPPER</li>
          <li class="accent">SEGMENTATION</li>
          <li>ONLINE COMMUNITIES</li>
          <li>CUSTOMER EXPERIENCE</li>
          <li>VISUALISATION</li>
          <li class="accent">TAILOR MADE</li>
        </ul>
      </li>
      <li class="nav-main">CONTACT US</li>
    </ul>
    <div class="newsletter">
      <h3>STAY IN THE KNOW</h3>
      <div class="signup">
        <span>Enter email:</span>
        <svg width="23" height="23" viewBox="0 0 23 23"><circle cx="11.5" cy="11.5" r="11" fill="#fdcc0a"/><path d="M9.5 7 L14 11.5 L9.5 16" fill="none" stroke="#fff" stroke-width="2"/></svg>
      </div>
    </div>
    <div class="copyright">© 2013 Tusk. All Rights Reserved.</div>
  </aside>

  <div class="gallery">
    <div class="tile" role="img" aria-label="Photo of a smiling customer"></div>
    <div class="tile" role="img" aria-label="Photo of a smiling customer"></div>
    <div class="tile" role="img" aria-label="Photo of a smiling customer"></div>
    <div class="tile" role="img" aria-label="Photo of a smiling customer"></div>
    <div class="tile" role="img" aria-label="Photo of a smiling customer"></div>
    <div class="tile" role="img" aria-label="Photo of a smiling customer"></div>
    <div class="tile" role="img" aria-label="Photo of a smiling customer"></div>
    <div class="tile" role="img" aria-label="Photo of a customer wearing glasses"></div>
    <div class="tile" role="img" aria-label="Photo of a smiling customer"></div>
  </div>

  <section class="modal">
    <header class="modal-head"><h1>WHAT WE DO</h1></header>
    <div class="close"><svg width="26" height="25" viewBox="0 0 26 25"><path d="M8 7.5 L18 17.5 M18 7.5 L8 17.5" stroke="#fff" stroke-width="1.2"/></svg></div>
    <div class="modal-body">
      <p>From idea screening to the final product – we’ve got it covered!&nbsp; We provide commercial recommendations to help clients generate more successful product launches whether it’s concept, product, packaging, claims, price evaluation or full mix optimisation.</p>
      <p><strong>CONCEPT:</strong><br>We can evaluate a mass of early stage ideas and identify the strongest ideas for further consideration, as well as optimisemore developed concepts.&nbsp; All ideas can be tested quickly and cost-efficiently online, either at general population level or among a more focused target group. We use tried and tested key measures and often overlay more interactive techniques to obtain detailed diagnostic information to help optimise your ideas to ensure they have the greatest possible appeal.&nbsp; We can provide clarity on whether a concept has the potential to succeed in market, who the target audience should be, where source of volume will come from, and understand what variants would optimise the range.</p>
      <p><strong>CLAIMS:</strong><br>We can understand which claims resonate best with your target audience, and specific segments within the total population.&nbsp; Claims are often evaluated through choice exercises so the relative strength of different claims can be understood and tested with appropriate context.</p>
      <p><strong>PRICING:</strong><br>We use a range of approaches to understand pricing depending on the stage of testing.&nbsp; These range from the more pragmatic techniques such as PSM (Halvorsen) or monadic (control group) testing, through to more sophisticated choice based methods.</p>
    </div>
    <div class="scrollbar"></div>
    <footer class="modal-foot"></footer>
  </section>
</div>
</body>
</html>
```